Personal Website for DBA of my main company

I need a website created for my personal brand for one of my DBA's of my main company. This website will be about my personal passion of wine. I am a certified sommelier and want a page that shows my passions for the wine industry. It will consist of pages that have video, pictures and possibly links to my cellar. (I have uploaded a screen shot of the only page I could find from a sommelier, I do not want to copy or look anything like this page....its just an idea of what one would look like)

Target Market(s)

Small, mostly word of mouth customers

Industry/Entity Type

Wine and Service Industry

Coding

Coded - Design and coding required

Number of Pages Required

4 page

Font styles to use
Other font styles liked:
• Font that is current but will be relevant in the future as well

Colors
0054AA
0677BA
7BADD7
CADEEF
E8F1F8
0094D4
00A9DD
6FCCEA
C7EBF8
E9F6FB
00AB8E
00BBA5
67D7C9
C6EFE9
E9F9F6
EB3D1F
EC4F4E
F09395
F8D3D4
FCEDEE

Requirements
Must have
• Landing page, video page and images page.

```html
<!DOCTYPE html>
<html lang="en">
<head>
<meta charset="utf-8">
<title>Cellar Notes – My personal passion for wine</title>
<link href="https://fonts.googleapis.com/css2?family=Playfair+Display:wght@400;600;700&family=Mulish:wght@400;600;700;800&display=swap" rel="stylesheet">
<style>
:root{
  --ink:#1c1c1f;
  --text:#3a3a3f;
  --green:#14896c;
  --green-light:#00ab8e;
  --navy:#0054aa;
  --frame:#2d4a78;
  --frame-light:#7badd7;
  --mist:#f2f2f5;
  --sky:#8ad2f1;
  --night:#1d1e21;
  --white:#ffffff;
  --serif:'Playfair Display', Georgia, serif;
  --sans:'Mulish', Arial, sans-serif;
}
*{box-sizing:border-box;margin:0;padding:0}
html,body{width:1200px;height:4975px;overflow:hidden}
body{position:relative;background:var(--white);font-family:var(--sans);color:var(--text)}
.abs{position:absolute}
a{color:inherit;text-decoration:none}

/* nav */
.brand{font-family:var(--serif);font-weight:600;font-size:30px;color:var(--ink);letter-spacing:.5px}
.site-nav{position:absolute;top:26px;left:586px;font-size:14px;color:var(--ink)}
.site-nav a{position:absolute;white-space:nowrap}
.site-nav a.is-active{color:var(--green)}
.site-nav a.is-active::after{content:"";position:absolute;left:0;right:0;bottom:-8px;height:2px;background:var(--green)}

/* buttons */
.btn{position:absolute;display:flex;align-items:center;justify-content:center;background:var(--green);color:var(--white);font-weight:800;font-size:12px;letter-spacing:.6px;text-transform:uppercase}

/* bracket heading */
.frame-title{position:absolute;display:flex;align-items:center;justify-content:center;font-family:var(--serif);font-weight:700;color:var(--ink);font-size:22px}
.frame-title::before,.frame-title::after{content:"";position:absolute;top:0;bottom:0;width:60%;border:2px solid var(--frame)}
.frame-title::before{left:0;border-right:none;border-bottom-color:transparent}
.frame-title::after{right:0;border-left:none;border-top-color:transparent}

/* hero */
.hero-title{font-family:var(--serif);font-weight:700;font-size:48px;line-height:52px;color:var(--ink)}
.hero-lead{font-size:15px;line-height:26px;color:var(--text)}

/* services */
.band-mist{background:var(--mist)}
.service-card{position:absolute;width:282px;height:380px;background:var(--white);box-shadow:0 4px 14px rgba(0,0,0,.08);text-align:center}
.service-card .icon-frame{position:absolute;left:70px;top:40px;width:142px;height:58px}
.service-card .icon-frame::before,.service-card .icon-frame::after{content:"";position:absolute;top:0;bottom:0;width:16px;border:2px solid var(--frame-light)}
.service-card .icon-frame::before{left:0;border-right:none}
.service-card .icon-frame::after{right:0;border-left:none}
.service-card svg{position:absolute;left:50%;top:50%;transform:translate(-50%,-50%)}
.service-card h3{position:absolute;top:132px;left:0;right:0;font-family:var(--serif);font-weight:700;font-size:15px;color:var(--ink)}
.service-card p{position:absolute;top:174px;left:30px;right:30px;font-size:11.2px;line-height:17.5px;color:var(--text)}
.service-card .btn{left:101px;top:324px;width:88px;height:25px;font-size:10.5px}

/* about */
.about-frame{position:absolute;left:616px;top:1846px;width:450px;height:400px;border-top:2px solid var(--frame);border-right:2px solid var(--frame);border-bottom:2px solid var(--frame)}
.about-copy{font-size:13px;line-height:20px;text-align:justify;color:var(--text)}

/* tastings */
.centered-copy{font-size:15px;line-height:26px;text-align:center;color:var(--text)}

/* club */
.club-copy{font-size:15.5px;line-height:25px;color:var(--ink)}

/* posts */
.post-card{position:absolute;width:294px;height:410px;background:var(--white);box-shadow:0 4px 14px rgba(0,0,0,.08)}
.post-card .post-image{position:absolute;left:0;top:0;width:294px;height:188px}
.post-card h3{position:absolute;left:28px;right:24px;top:206px;font-family:var(--serif);font-weight:400;font-size:16px;line-height:25px;color:var(--ink)}
.post-card p{position:absolute;left:28px;right:24px;top:292px;font-size:11.5px;line-height:16px}
.post-card .more{position:absolute;left:28px;top:348px;font-size:10.5px;font-weight:800;color:var(--green);letter-spacing:.5px;border-bottom:1px solid var(--green)}

/* contact */
.field{position:absolute;height:43px;border:1px solid #8a8a90;background:rgba(255,255,255,.55);font-size:12px;color:var(--ink);padding:16px 18px 0}
.field.message{height:106px}

/* footer */
.footer{position:absolute;left:0;top:4782px;width:1200px;height:193px;background:var(--night);color:var(--white)}
.footer-nav a{position:absolute;top:54px;font-size:14px;color:#e8e8ea;white-space:nowrap}
.footer .rule{position:absolute;left:128px;right:132px;top:106px;height:1px;background:#3a3b40}
.social{position:absolute;top:140px;width:22px;height:22px;border-radius:4px;background:#f2f2f2}
</style>
</head>
<body>

<header>
  <div class="abs brand" style="left:131px;top:20px">Cellar Notes</div>
  <nav class="site-nav">
    <a class="is-active" style="left:0">Home</a>
    <a style="left:75px">About Us</a>
    <a style="left:173px">Services</a>
    <a style="left:261px">Wine</a>
    <a style="left:338px">Blog</a>
    <a style="left:407px">Contact Us</a>
  </nav>
</header>

<section class="hero">
  <svg class="abs" style="left:0;top:0" width="1200" height="760" viewBox="0 0 1200 760">
    <defs>
      <linearGradient id="heroTone" x1="0" y1="0" x2="0.6" y2="1">
        <stop offset="0" stop-color="#6d7c92"/>
        <stop offset="0.45" stop-color="#3f5a8c"/>
        <stop offset="1" stop-color="#4a3a30"/>
      </linearGradient>
    </defs>
    <rect x="0" y="0" width="1200" height="760" fill="var(--white)"/>
    <polygon points="0,745 1200,648 1200,760 0,760" fill="var(--mist)"/>
    <path d="M0,430 L170,380 L250,110 L560,95 L760,140 L770,560 L1200,540 L1200,648 L0,745 Z" fill="url(#heroTone)" role="img" aria-label="Illustrated portrait of the sommelier at a table, holding a bottle of white wine and sipping from a cup"/>
    <polygon points="0,742 1200,645 1200,672 0,750" fill="var(--navy)"/>
  </svg>
  <h1 class="abs hero-title" style="left:808px;top:142px;width:290px">My personal passion for wine</h1>
  <p class="abs hero-lead" style="left:808px;top:320px;width:270px">Lorem Ipsum is simply dummy text of the printing and typesetting</p>
  <a class="btn" style="left:813px;top:402px;width:118px;height:36px">Read More</a>
</section>

<section>
  <div class="abs band-mist" style="left:0;top:760px;width:1200px;height:1020px"></div>
  <h2 class="frame-title" style="left:510px;top:759px;width:178px;height:55px">Our Services</h2>

  <article class="service-card" style="left:149px;top:860px">
    <div class="icon-frame"><svg width="44" height="44" viewBox="0 0 44 44" fill="none" stroke="var(--navy)" stroke-width="2"><path d="M8 4h8l-1 8a3 3 0 0 1-6 0z M28 4h8l-1 8a3 3 0 0 1-6 0z M12 15v6 M32 15v6"/><rect x="4" y="22" width="36" height="12"/><path d="M22 34v6 M14 40h16"/></svg></div>
    <h3>Private Dinners</h3>
    <p>There are many variations of pas sages of Lorem Ipsum available, but the majority have suffered alteration in some form, by injected humour, or randomised words which don't look even slightly believable. If you are going to use a passage.</p>
    <a class="btn">Read More</a>
  </article>
  <article class="service-card" style="left:460px;top:860px">
    <div class="icon-frame"><svg width="44" height="44" viewBox="0 0 44 44" fill="none" stroke="var(--navy)" stroke-width="2"><path d="M6 20h12l-1 7a5 5 0 0 1-10 0z M12 32v8 M7 40h10"/><path d="M28 4h6v8l4 6v22H24V18l4-6z" fill="var(--navy)"/></svg></div>
    <h3>Wine Consultations</h3>
    <p>There are many variations of pas sages of Lorem Ipsum available, but the majority have suffered alteration in some form, by injected humour, or randomised words which don't look even slightly believable. If you are going to use a passage.</p>
    <a class="btn">Read More</a>
  </article>
  <article class="service-card" style="left:773px;top:860px">
    <div class="icon-frame"><svg width="44" height="44" viewBox="0 0 44 44" fill="none" stroke="var(--navy)" stroke-width="2"><rect x="4" y="8" width="36" height="32" rx="2"/><path d="M4 16h36 M12 4v8 M32 4v8"/><path d="M10 22h4 M18 22h4 M26 22h4 M10 28h4 M18 28h4 M26 28h4 M10 34h4 M18 34h4 M26 34h4"/></svg></div>
    <h3>Monthly Maintenance</h3>
    <p>There are many variations of pas sages of Lorem Ipsum available, but the majority have suffered alteration in some form, by injected humour, or randomised words which don't look even slightly believable. If you are going to use a passage.</p>
    <a class="btn">Read More</a>
  </article>
  <article class="service-card" style="left:149px;top:1271px">
    <div class="icon-frame"><svg width="48" height="44" viewBox="0 0 48 44" fill="none" stroke="var(--navy)" stroke-width="2"><path d="M10 4h4v6l2 3v9H8v-9l2-3z M22 4h4v6l2 3v9h-8v-9l2-3z M34 4h4v6l2 3v9h-8v-9l2-3z"/><rect x="3" y="22" width="42" height="18"/><path d="M3 31h42"/></svg></div>
    <h3>Sell Your Cellar</h3>
    <p>There are many variations of pas sages of Lorem Ipsum available, but the majority have suffered alteration in some form, by injected humour, or randomised words which don't look even slightly believable. If you are going to use a passage.</p>
    <a class="btn">Read More</a>
  </article>
  <article class="service-card" style="left:460px;top:1271px">
    <div class="icon-frame"><svg width="48" height="44" viewBox="0 0 48 44" fill="none" stroke="var(--navy)" stroke-width="2"><path d="M6 8h12l-1 8a5 5 0 0 1-10 0z M12 21v8 M7 29h10"/><path d="M26 16h12l-1 8a5 5 0 0 1-10 0z M32 29v8 M27 37h10"/></svg></div>
    <h3>Wine Tastings</h3>
    <p>There are many variations of pas sages of Lorem Ipsum available, but the majority have suffered alteration in some form, by injected humour, or randomised words which don't look even slightly believable. If you are going to use a passage.</p>
    <a class="btn">Read More</a>
  </article>
  <div class="abs" style="left:770px;top:1271px;width:286px;height:382px;background:linear-gradient(160deg,#4a4036 0%,#2e2b2c 45%,#8c2a2e 75%,#3a3034 100%)" role="img" aria-label="Illustrated photo of the sommelier holding up a red cup"></div>
</section>

<section>
  <div class="abs" style="left:116px;top:1729px;width:456px;height:610px;background:linear-gradient(180deg,#e9eef5 0%,#6d8ac2 40%,#2f4f92 75%,#d8cdb4 100%);border-radius:40% 40% 6px 6px / 18% 18% 6px 6px" role="img" aria-label="Illustrated figure of the sommelier in a blue jacket checking his phone, a wine bottle in his pocket"></div>
  <div class="about-frame"></div>
  <h2 class="frame-title" style="left:506px;top:1816px;width:180px;height:58px;background:var(--white)">About Me</h2>
  <div class="abs about-copy" style="left:616px;top:1914px;width:394px">
    <p>There are many variations of passages of Lorem Ipsum available, but the majority have suffered alteration in some form, by injected humour, or randomised words which don't look even slightly believable. If you are going to use a passage of Lorem Ipsum, you need to be sure there isn't anything embarrassing hidden in the middle of text. All the Lorem Ipsum generators on the Internet tend to repeat predefined chunks as necessary, making this the first true generator</p>
    <p style="margin-top:22px">If you are going to use a passage of Lorem Ipsum, you need to be sure there isn't anything embarrassing hidden in the middle of text. All the Lorem Ipsum generators on the Internet tend to repeat predefined chunks as necessary.</p>
  </div>
  <a class="btn" style="left:916px;top:2231px;width:96px;height:27px;font-size:11px">Read More</a>
</section>

<section>
  <svg class="abs" style="left:0;top:2310px" width="1200" height="620" viewBox="0 0 1200 620">
    <polygon points="0,30 1200,8 1200,620 0,620" fill="var(--mist)"/>
    <polygon points="0,24 1200,0 1200,10 0,44" fill="var(--navy)"/>
  </svg>
  <h2 class="frame-title" style="left:510px;top:2401px;width:180px;height:56px">Wine Tastings</h2>
  <p class="abs centered-copy" style="left:200px;top:2496px;width:800px">There are many variations of passages of Lorem Ipsum available, but the majority have suffered alteration in some form, by injected humour, or randomised words which don't look even slightly believable. If you are going to use a passage of Lorem Ipsum, you need to be sure there isn't anything embarrassing hidden in the middle of text. All the Lorem Ipsum generators on the Internet tend to repeat predefined.</p>
  <a class="btn" style="left:553px;top:2635px;width:96px;height:27px;font-size:11px">Read More</a>
  <div class="abs" style="left:0;top:2680px;width:1200px;height:248px;background:linear-gradient(180deg,rgba(242,242,245,0) 0%,rgba(200,200,206,.55) 70%,rgba(170,170,178,.7) 100%)" role="img" aria-label="Line sketch of wine bottles, glasses, grapes, corks and cheese"></div>
</section>

<section>
  <svg class="abs" style="left:0;top:2908px" width="1200" height="700" viewBox="0 0 1200 700">
    <polygon points="0,20 1200,0 1200,650 0,640" fill="var(--sky)"/>
    <polygon points="0,640 1200,614 1200,700 0,700" fill="var(--white)"/>
    <polygon points="0,628 1200,586 1200,616 0,668" fill="var(--night)"/>
  </svg>
  <div class="abs" style="left:425px;top:3033px;width:775px;height:540px;background:linear-gradient(200deg,#f2c9a6 0%,#c68d6a 35%,#3d2e2a 60%,#141a2c 100%);clip-path:polygon(40% 0,100% 0,100% 100%,0 100%,30% 70%)" role="img" aria-label="Illustrated portrait of the sommelier in glasses and a dark jacket"></div>
  <h2 class="frame-title" style="left:131px;top:3004px;width:248px;height:56px">Join the Wine Club!</h2>
  <p class="abs club-copy" style="left:128px;top:3118px;width:400px">There are many variations of passages of Lorem Ipsum available, but the majority have suffered alteration in some form, by injected humour, or randomised words which don't look even slightly believable. If you are going to use a passage of Lorem Ipsum, you need to be sure there isn't anything embarrassing hidden in the middle of text. All the Lorem Ipsum generators on the Internet tend to repeat predefined.</p>
  <a class="btn" style="left:128px;top:3362px;width:100px;height:29px;font-size:11px">Read More</a>
</section>

<section>
  <h2 class="frame-title" style="left:506px;top:3636px;width:180px;height:56px">Recent Posts</h2>

  <article class="post-card" style="left:128px;top:3735px">
    <div class="post-image" style="background:linear-gradient(150deg,#2a0e0e 0%,#7a1c1c 45%,#c47a52 100%)" role="img" aria-label="Red wine being poured into a glass"></div>
    <h3>Lorem Ipsum is simply dummy text of the printing and types etting industry.</h3>
    <p>If you are going to use a passage of Lorem Ipsum, you need to be sure there isn't anything embarrassing.</p>
    <a class="more">READ MORE</a>
  </article>
  <article class="post-card" style="left:451px;top:3735px">
    <div class="post-image" style="background:linear-gradient(150deg,#5a2a14 0%,#d98a3a 45%,#f3c98a 100%)" role="img" aria-label="Friends raising glasses of white wine in a toast"></div>
    <h3>Lorem Ipsum is simply dummy text of the printing and types etting industry.</h3>
    <p>If you are going to use a passage of Lorem Ipsum, you need to be sure there isn't anything embarrassing.</p>
    <a class="more">READ MORE</a>
  </article>
  <article class="post-card" style="left:774px;top:3735px">
    <div class="post-image" style="background:linear-gradient(180deg,#8fa6b8 0%,#4f7288 45%,#d9e2ea 100%)" role="img" aria-label="Wine bottle and glasses on a sunny lakeside shore"></div>
    <h3>Lorem Ipsum is simply dummy text of the printing and types etting industry.</h3>
    <p>If you are going to use a passage of Lorem Ipsum, you need to be sure there isn't anything embarrassing.</p>
    <a class="more">READ MORE</a>
  </article>
</section>

<section>
  <div class="abs" style="left:0;top:4208px;width:1200px;height:574px;background:linear-gradient(90deg,#d9c7b4 0%,#ece5dc 35%,#efe9e2 65%,#e3d3c6 100%)" role="img" aria-label="Faded illustrated group photo of friends sharing wine"></div>
  <h2 class="frame-title" style="left:516px;top:4250px;width:162px;height:54px;background:var(--white)">Contact Me</h2>
  <form>
    <div class="field" style="left:278px;top:4395px;width:314px">Full Name</div>
    <div class="field" style="left:609px;top:4395px;width:314px">Email</div>
    <div class="field" style="left:278px;top:4461px;width:314px">Phone</div>
    <div class="field" style="left:609px;top:4461px;width:314px">Subject</div>
    <div class="field message" style="left:278px;top:4521px;width:645px">Message</div>
    <a class="btn" style="left:556px;top:4650px;width:88px;height:29px;font-size:12px">Submit</a>
  </form>
</section>

<footer class="footer">
  <div class="abs brand" style="left:128px;top:48px;color:var(--white);font-size:32px">Cellar Notes</div>
  <nav class="footer-nav">
    <a style="left:577px">Home</a>
    <a style="left:654px">About Us</a>
    <a style="left:753px">Services</a>
    <a style="left:843px">Wine</a>
    <a style="left:924px">Blog</a>
    <a style="left:995px">Contact Us</a>
  </nav>
  <div class="rule"></div>
  <div class="abs" style="left:128px;top:144px;font-size:12px;color:#e8e8ea">Follow us</div>
  <span class="social" style="left:203px"></span>
  <span class="social" style="left:237px"></span>
  <span class="social" style="left:271px"></span>
  <div class="abs" style="left:865px;top:142px;font-size:12px;color:#e8e8ea">Copyright © 2022 All Rights Reserved</div>
</footer>

</body>
</html>
```